business card for author of crime novel

I am an author with a new book. I need a business card with the book's cover on one side (already uploaded), and contact details on the other.

Tom Velasquin
Author

telephone: 917-555-0162
website: www.tomvelasquin.example
facebook: facebook.com/tvelasquin
twitter: twitter.com/tvelasquin
email: tvelasquin@mailbox.example

Target Market(s)

Readers of mystery books

Industry/Entity Type

Business

Contact Information for Business Card

Tom Velasquin
Author

telephone: 917-555-0162

Font styles to use
Serif
Sans Serif

Requirements
Must have
• Book cover on one side. My contact info on the other, with the name of the book repeated if that makes sense. Clean design.
Should not have
• Overly ornate, too formal, too distracting

```html
<!DOCTYPE html>
<html lang="en">
<head>
<meta charset="utf-8">
<title>Tom Velasquin – Author Business Card</title>
<link rel="stylesheet" href="https://fonts.googleapis.com/css2?family=Special+Elite&family=Cinzel:wght@400;600&family=Tinos:wght@400;700&display=swap">
<style>
  :root {
    --backdrop: #9a9a9a;
    --card-mustard: #c8912e;
    --ink-black: #1a1510;
    --cover-name: #d9d56b;
    --photo-dark: #1f2e33;
    --photo-mid: #5f7c85;
    --photo-light: #a9c1c6;
    --label-paper: #e9d6a8;
    --label-edge: #cdb07a;
    --label-ink: #2a2016;
    --text-white: #fffaf0;
  }
  * { box-sizing: border-box; margin: 0; padding: 0; }
  html, body { width: 1200px; height: 875px; overflow: hidden; }
  body { background: var(--backdrop); position: relative; }

  .card {
    position: absolute;
    top: 185px;
    width: 341px;
    height: 533px;
    background: var(--card-mustard);
  }
  .card--front { left: 204px; }
  .card--back { left: 594px; }

  .book-title {
    position: absolute;
    top: 34px; left: 0; width: 100%;
    text-align: center;
    font-family: "Special Elite", "Courier New", monospace;
    font-size: 28px;
    letter-spacing: 1px;
    color: var(--ink-black);
    text-transform: uppercase;
  }
  .cover-photo {
    position: absolute;
    top: 86px; left: 30px;
    width: 268px; height: 352px;
    background: linear-gradient(160deg, var(--photo-light) 0%, var(--photo-mid) 40%, var(--photo-dark) 100%);
  }
  .cover-author {
    position: absolute;
    right: 6px; bottom: 20px;
    text-align: center;
    font-family: "Cinzel", "Times New Roman", serif;
    font-size: 17px;
    line-height: 1.05;
    color: var(--cover-name);
  }
  .series-label {
    position: absolute;
    top: 458px; left: 35px;
    width: 265px; height: 41px;
    background: var(--label-paper);
    border: 1px solid var(--label-edge);
    display: flex; align-items: center; justify-content: center;
    font-family: "Special Elite", "Courier New", monospace;
    font-size: 19px;
    color: var(--label-ink);
  }

  .contact-name {
    position: absolute;
    top: 74px; left: 0; width: 100%;
    text-align: center;
    font-family: "Tinos", "Times New Roman", serif;
    font-weight: 700;
    font-size: 20px;
    letter-spacing: 2px;
    color: var(--text-white);
    text-transform: lowercase;
  }
  .contact-role {
    position: absolute;
    top: 104px; left: 0; width: 100%;
    text-align: center;
    font-family: "Tinos", "Times New Roman", serif;
    font-size: 15px;
    letter-spacing: 3px;
    color: var(--text-white);
  }
  .contact-list {
    position: absolute;
    top: 348px; left: 0; width: 100%;
    list-style: none;
    text-align: center;
    font-family: "Tinos", "Times New Roman", serif;
    font-size: 15.5px;
    line-height: 25.5px;
    color: var(--text-white);
  }
</style>
</head>
<body>
  <section class="card card--front" aria-label="Book cover side">
    <h1 class="book-title">Dead Letter Alley</h1>
    <div class="cover-photo" role="img" aria-label="Blue-toned photograph of a tall brick tenement building with fire escapes">
      <p class="cover-author">TOM<br>VELASQUIN</p>
    </div>
    <p class="series-label">A Marlowe Quinn Mystery</p>
  </section>

  <section class="card card--back" aria-label="Contact side">
    <h2 class="contact-name">tom velasquin</h2>
    <p class="contact-role">author</p>
    <ul class="contact-list">
      <li>telephone: 917-555-0162</li>
      <li>website: www.tomvelasquin.example</li>
      <li>facebook: facebook.com/tvelasquin</li>
      <li>twitter: twitter.com/tvelasquin</li>
      <li>email: tvelasquin@mailbox.example</li>
    </ul>
  </section>
</body>
</html>
```